Lanternfield Disability - Social Security Disability Attorneys

Our company is expanding to attract clients nationwide for our social security disability practice. We have a logo, but I am looking for a creative and elegant letterhead that projects an image of being technologically advanced but still professional enough for the legal field. I am looking for the "wow factor" combined with this is still professional enough for a law practice.

Requesting letterhead and business card design
Updates

Had to update and change the logo. The previous logo had a typo. Please send updates with the new logo for consideration. The letterhead and business cards should be professional enough to be used for a law firm. Thanks.

Industry/Entity Type

Law Practice, Law Firm, Healthcare Industry, Government

Colors

Designer to choose colors to be used in the design.

Requirements
Nice to have
• **Please create a vertical design for the business card**

```html
<!DOCTYPE html>
<html lang="en">
<head>
<meta charset="utf-8">
<title>Lanternfield Disability – Letterhead and Business Card</title>
<link href="https://fonts.googleapis.com/css2?family=Roboto+Condensed:wght@300;400;500&display=swap" rel="stylesheet">
<style>
  :root {
    --blue-deep: #0660dc;
    --blue-mid: #2a92ea;
    --blue-sky: #48ddfd;
    --brand-blue: #4a78e4;
    --orange: #ff6a08;
    --ink: #1a1a1a;
    --paper: #ffffff;
    --mist: #e7eded;
  }
  html, body { margin: 0; padding: 0; overflow: hidden; background: var(--paper); }
  .sheet {
    position: relative;
    width: 849px; height: 1200px;
    overflow: hidden;
    background: var(--paper);
    font-family: "Roboto Condensed", "Arial Narrow", sans-serif;
    color: var(--ink);
  }
  .shapes { position: absolute; inset: 0; }
  .text { position: absolute; margin: 0; white-space: nowrap; }

  .brand-name {
    color: var(--brand-blue);
    font-weight: 500;
    text-transform: uppercase;
    letter-spacing: 0.12em;
  }
  .letterhead-brand { left: 46px; width: 270px; top: 110px; font-size: 17.5px; text-align: center; }
  .brand-mist { left: 128px; right: 0; top: 620px; font-size: 46px; text-align: center; color: var(--mist); }

  .contact-line { font-size: 13px; line-height: 14px; }
  .lh-address { left: 678px; top: 52px; }
  .lh-phone { left: 678px; top: 106px; }
  .lh-email { left: 678px; top: 134px; }

  .footer-tagline { right: 27px; top: 1142px; font-size: 21px; font-weight: 300; color: var(--paper); }

  .card-brand { left: 177px; width: 222px; top: 871px; font-size: 11.5px; text-align: center; }
  .card-name { left: 177px; width: 222px; top: 911px; font-size: 16px; letter-spacing: 0.06em; text-align: center; font-weight: 300; }
  .card-title { left: 177px; width: 222px; top: 932px; font-size: 11px; letter-spacing: 0.05em; text-align: center; }
  .card-contact { left: 177px; width: 222px; font-size: 10px; line-height: 11px; text-align: center; }
  .card-address { top: 991px; }
  .card-phone { top: 1035px; }
  .card-email { top: 1069px; }
  .card-tagline { left: 189px; top: 1146px; font-size: 10px; color: var(--paper); }

  .corner-accent {
    position: absolute;
    background: linear-gradient(160deg, var(--blue-sky), var(--blue-mid) 55%, var(--blue-deep));
    opacity: 0.85;
  }
  .letterhead-accent { left: 801px; top: 1028px; width: 48px; height: 98px; }
  .card-accent { left: 367px; top: 1125px; width: 31px; height: 50px; }
</style>
</head>
<body>
<div class="sheet">
  <svg class="shapes" width="849" height="1200" viewBox="0 0 849 1200" aria-hidden="true">
    <defs>
      <linearGradient id="side-band" x1="0" y1="0" x2="0.25" y2="1">
        <stop offset="0" stop-color="var(--blue-deep)"/>
        <stop offset="0.45" stop-color="var(--blue-mid)"/>
        <stop offset="1" stop-color="var(--blue-sky)"/>
      </linearGradient>
      <linearGradient id="edge-bar" x1="0" y1="0" x2="0" y2="1">
        <stop offset="0" stop-color="var(--blue-sky)"/>
        <stop offset="1" stop-color="var(--blue-deep)"/>
      </linearGradient>
      <linearGradient id="card-frame" x1="0" y1="0" x2="1" y2="0.4">
        <stop offset="0" stop-color="var(--blue-sky)"/>
        <stop offset="1" stop-color="var(--blue-mid)"/>
      </linearGradient>
      <g id="pin"><path d="M0 -5 a4 4 0 0 1 4 4 c0 3 -4 7 -4 7 c0 0 -4 -4 -4 -7 a4 4 0 0 1 4 -4z" fill="var(--blue-mid)"/><circle cx="0" cy="-1" r="1.5" fill="var(--paper)"/></g>
      <g id="phone"><path d="M-4 -5 l2 -1 l2 3 l-1.5 1.2 c0.8 2 2 3.2 4 4 l1.2 -1.5 l3 2 l-1 2 c-5 0 -10 -5 -9.7 -9.7z" fill="var(--blue-sky)"/></g>
      <g id="mail"><rect x="-6" y="-4" width="12" height="8" fill="var(--blue-sky)"/><path d="M-6 -4 l6 5 l6 -5 M-6 4 l4.5 -4 M6 4 l-4.5 -4" stroke="var(--paper)" stroke-width="0.8" fill="none"/></g>
    </defs>

    <!-- letterhead side band -->
    <rect x="0" y="0" width="116" height="1200" fill="url(#side-band)"/>
    <rect x="116" y="0" width="12" height="1200" fill="var(--orange)"/>
    <rect x="46" y="48" width="82" height="104" fill="var(--paper)"/>

    <!-- right edge accent -->
    <rect x="841" y="52" width="8" height="92" fill="url(#edge-bar)"/>

    <!-- contact icons -->
    <use href="#pin" x="667" y="60"/>
    <use href="#phone" x="666" y="116"/>
    <use href="#mail" x="665" y="141"/>

    <!-- footer band -->
    <polygon points="488,1168 521,1128 849,1128 849,1168" fill="var(--orange)"/>

    <!-- business card -->
    <rect x="177" y="812" width="222" height="376" fill="var(--paper)"/>
    <path d="M177 812 H399 V902 C393 897 385 892 378 888 V829 H198 V888 C191 891 183 897 177 902 Z" fill="url(#card-frame)"/>
    <rect x="177.5" y="812.5" width="221" height="375" fill="none" stroke="var(--ink)" stroke-width="1"/>
    <rect x="177" y="1012" width="5" height="47" fill="url(#edge-bar)"/>
    <rect x="394" y="1012" width="5" height="47" fill="url(#edge-bar)"/>
    <use href="#pin" x="288" y="984"/>
    <use href="#phone" x="287" y="1028"/>
    <use href="#mail" x="288" y="1063"/>
    <polygon points="177,1142 334,1142 350,1161 177,1161" fill="var(--orange)"/>
  </svg>

  <div class="corner-accent letterhead-accent" role="img" aria-label="Decorative blue folded-ribbon graphic in the page corner"></div>
  <div class="corner-accent card-accent" role="img" aria-label="Decorative blue folded-ribbon graphic in the card corner"></div>

  <!-- letterhead -->
  <p class="text brand-name letterhead-brand">Lanternfield Disability</p>
  <p class="text brand-name brand-mist">Lanternfield Disability</p>

  <p class="text contact-line lh-address">1111 xxxxx xxx xxxxx<br>xxxxxxxx xxx<br>xxxxx 00000</p>
  <p class="text contact-line lh-phone">(000) 0000 0000</p>
  <p class="text contact-line lh-email">info@xxxxxxxxxxxxxxxxx.com</p>

  <p class="text footer-tagline">Social Security Disability Attorneys</p>

  <!-- business card -->
  <p class="text brand-name card-brand">Lanternfield Disability</p>
  <p class="text card-name">AXXXXX MXXXXXX</p>
  <p class="text card-title">ATTORNEY</p>
  <p class="text card-contact card-address">1111 xxxxx xxx xxxxx<br>xxxxxxxx xxx&nbsp; xxxxx 00000</p>
  <p class="text card-contact card-phone">(000) 0000 0000</p>
  <p class="text card-contact card-email">info@xxxxxxxxxxxxxxxxx.com</p>
  <p class="text card-tagline">Social Security Disability Attorneys</p>
</div>
</body>
</html>
```